Under The Lanterns a Tola Rin Project - Not for profit project

I am looking for a basic template to use on webnode.
The site is for a charitable organization aimed at adults and importantly children. I have attached the copy. The theme of Tola Rin ( Tola Meadow in Spanish) is our family initials and the idea is to make it fun or at least interesting. We will translate the site to Spanish also. The power of waves and the power of a Greek god like Poseidon could be a good fit in developing the idea of creating waves of positive change. BUT the Wave theme and Poseidon need to be bright colours fun and inspiring. I dont want the site to look like a fantasy novel cover. Or a display of some amazing mans body as that is not the fit. Poseidon could be illustrated version. The SHORE FOLK drawing is something my daughter did and is fun and could work to engage , who will ultimately be the one to drive this project forward. But the “SHORE FOLK” is not mandatory.
I would prefer if the colors are not dark or depressing. In fact this is one of the reasons I am looking for a designer - so that the designer can find a way to present the wave theme but in a bright, uplifting tone.

I will use webnode templates so I am guessing the design would be in the form of background graphics that can be used on the webnode platform. But I need your suggestions on this ?

Target Market(s)

Anyone interested in creating a fairer world

Industry/Entity Type

Democracy

Number of Pages Required

3 page

Requirements
Must have
• Basic template -
Nice to have
• None are essential but ; Waves, SHORE FOLK, Poisedon or other greek gods

```html
<!DOCTYPE html>
<html lang="en">
<head>
<meta charset="utf-8">
<title>Under The Lanterns – A Tola Sea Fund</title>
<link rel="stylesheet" href="https://fonts.googleapis.com/css2?family=Cormorant+Garamond:wght@400;500&family=Urbanist:wght@400;800&display=swap">
<style>
:root{
  --teal:#33a9c0;
  --heading:#2c6d8a;
  --ink:#1d2a33;
  --white:#ffffff;
  --bar:#2f8fab;
  --hero-light:#8fdbe3;
  --hero-mid:#4cb6c9;
  --hero-deep:#2a8ea9;
  --band-top:#6aaed8;
  --band-bottom:#3f8cc0;
  --sea-top:#3eb3c8;
  --sea-bottom:#2a8caa;
  --line:rgba(255,255,255,.6);
}
*{box-sizing:border-box;margin:0;padding:0}
html,body{width:1200px;height:3636px;overflow:hidden;background:var(--white)}
body{font-family:"Urbanist",sans-serif;color:var(--ink);position:relative}
.page{position:relative;width:1200px;height:3636px;overflow:hidden}
.abs{position:absolute}
.serif{font-family:"Cormorant Garamond",serif;font-weight:400}
.btn{position:absolute;display:flex;align-items:center;justify-content:center;height:31px;border-radius:16px;background:var(--teal);color:var(--white);font-family:"Cormorant Garamond",serif;font-size:11px}
.btn.light{background:var(--white);color:var(--teal)}
.hero .btn{background:var(--white);color:var(--hero-deep)}

/* top bar */
.topbar{top:0;left:0;width:1200px;height:36px;background:var(--bar);color:var(--white);font-size:10px}
.topbar .social{left:122px;top:12px;display:flex;gap:12px}
.topbar .info{right:122px;top:12px;display:flex;gap:12px;align-items:center}
.sep{opacity:.8}

/* hero */
.hero-photo{top:36px;left:0;width:1200px;height:610px;background:radial-gradient(ellipse at 68% 35%,var(--hero-light) 0%,var(--hero-mid) 40%,var(--hero-deep) 100%)}
.nav{top:66px;left:122px;width:956px;height:32px;display:flex;align-items:center;color:var(--white)}
.brand{font-weight:800;font-size:22px;letter-spacing:.5px;color:var(--white)}
.nav ul{list-style:none;display:flex;gap:39px;margin-left:auto;margin-right:42px;font-size:12px}
.lang{width:100px;height:31px;border:1px solid var(--white);border-radius:16px;display:flex;align-items:center;justify-content:center;font-family:"Cormorant Garamond",serif;font-size:10px}
.hero-title{top:207px;left:122px;color:var(--white);font-size:56px;line-height:64px}
.hero-text{top:359px;left:122px;width:365px;color:var(--white);font-size:12.5px;line-height:19px}

/* mission */
.illus{top:790px;left:120px;width:480px;height:320px;border-radius:8px;background:linear-gradient(135deg,#eef8fa,#d6eff4)}
.mission-title{top:728px;left:632px;font-size:44px;color:var(--heading)}
.mission-text{top:803px;left:632px;width:440px;font-size:11.8px;line-height:18.8px}
.mission-text p+p{margin-top:18.8px}

/* values */
.values-title{top:1290px;left:122px;font-size:44px;color:var(--white)}
.values-list{top:1368px;left:122px;width:360px;color:var(--white)}
.value{border-bottom:1px solid var(--line);padding:4px 0 12px;margin-bottom:9px}
.value:last-child{border:none;width:400px}
.value h3{font-weight:400;font-size:17px;margin-bottom:6px}
.value h3 span{font-family:"Cormorant Garamond",serif;font-size:17px;margin-left:34px}
.value p{font-size:11.5px;line-height:19px;max-width:330px}
.value:last-child p{max-width:400px}
.values-photo{top:1300px;left:550px;width:528px;height:554px;background:linear-gradient(170deg,#9cc8e6 0%,#5c9cc9 40%,#a7d0e6 65%,#f1f8fb 100%)}

/* specifics */
.center{left:0;width:1200px;text-align:center}
.section-title{font-size:44px;color:var(--heading)}
.sub{font-size:11.5px}
.support{top:2138px;display:flex;position:absolute;left:225px;width:750px}
.support-item{width:250px;text-align:center;font-size:11.5px;line-height:19px;padding:0 10px}
.support-item svg{display:block;margin:0 auto 9px}

/* blog */
.card{position:absolute;top:2625px;width:306px;color:var(--white)}
.card .img{height:203px}
.card .date{font-size:11.5px;margin-top:14px}
.card h4{font-weight:400;font-size:17.5px;line-height:25px;margin-top:8px}
.card p{font-size:11px;margin-top:8px}

/* footer */
.footer-nav{top:3490px;left:122px;width:956px;display:flex;align-items:center;color:var(--white)}
.footer-nav .brand{font-size:34px}
.footer-nav ul{list-style:none;display:flex;gap:46px;margin-left:auto;font-size:14px}
.footer-rule{top:3578px;left:122px;width:956px;height:1px;background:var(--line)}
.copyright{top:3604px;font-size:11.5px;color:var(--white)}
</style>
</head>
<body>
<div class="page">

  <div class="abs hero-photo" role="img" aria-label="Stone statue resting in bright sunlit shallow water"></div>

  <svg class="abs" style="top:0;left:0" width="1200" height="3636" viewBox="0 0 1200 3636" aria-hidden="true">
    <defs>
      <linearGradient id="bandFill" x1="0" y1="0" x2="0" y2="1">
        <stop offset="0" stop-color="#6aaed8"/><stop offset="1" stop-color="#3f8cc0"/>
      </linearGradient>
      <linearGradient id="seaFill" x1="0" y1="0" x2="0" y2="1">
        <stop offset="0" stop-color="#3eb3c8"/><stop offset="1" stop-color="#2a8caa"/>
      </linearGradient>
    </defs>
    <path d="M0 596 C120 585 170 640 300 630 S520 592 650 605 S880 650 1000 625 S1140 585 1200 590 L1200 650 L0 650Z" fill="#fff"/>
    <path d="M0 1245 C90 1230 140 1180 260 1190 S440 1250 560 1230 S760 1180 880 1200 S1080 1250 1200 1220 L1200 1905 C1100 1935 1000 1960 880 1945 S650 1895 520 1915 S260 1965 150 1950 S40 1920 0 1925Z" fill="url(#bandFill)"/>
    <path d="M0 2425 C120 2430 180 2385 300 2395 S480 2460 600 2450 S800 2385 920 2395 S1110 2440 1200 2420 L1200 3005 C1100 3030 1000 3060 880 3045 S650 2995 520 3015 S260 3070 150 3045 S40 3010 0 3025Z" fill="url(#seaFill)"/>
    <path d="M0 3420 C110 3395 190 3360 310 3375 S500 3410 620 3390 S820 3350 940 3370 S1120 3400 1200 3380 L1200 3636 L0 3636Z" fill="url(#seaFill)"/>
  </svg>

  <div class="abs topbar">
    <div class="abs social"><span>Feed</span><span class="sep">|</span><span>Photos</span><span class="sep">|</span><span>Posts</span></div>
    <div class="abs info"><span>Address : TRF On a shore waiting for the waves to arrive.</span><span class="sep">|</span><span>Email : hello@tolarin.org</span><span class="sep">|</span>
      <svg width="11" height="11" viewBox="0 0 12 12"><circle cx="6" cy="6" r="5" fill="none" stroke="#fff"/><path d="M1 6h10M6 1c-2 2-2 8 0 10M6 1c2 2 2 8 0 10" fill="none" stroke="#fff"/></svg></div>
  </div>

  <div class="hero">
    <header class="abs nav">
      <span class="brand">SHORE FOLK</span>
      <ul><li>HOME</li><li>MISSION</li><li>WHO</li><li>FOCUS</li><li>BLOG</li><li>CONTACT</li></ul>
      <span class="lang">Espanol</span>
    </header>
    <h1 class="abs hero-title serif">Under The Lanterns<br>A Tola Sea Fund</h1>
    <p class="abs hero-text">Never doubt that a small group of committed citizens can change the world; in fact, it is the only thing that has ever done so.</p>
    <span class="btn" style="top:422px;left:122px;width:125px">Discover Our Mission</span>
  </div>

  <div class="abs illus" role="img" aria-label="Line drawing of a surfer riding a wave"></div>
  <h2 class="abs mission-title serif">Mission &amp; Vision</h2>
  <div class="abs mission-text">
    <p>Under the Lanterns champions democratic solutions for the pressing issues facing our world. These solutions must promote justice, equality, environmental responsibility, and the inherent worth of every person, in order to create a more just and equitable world for all.<br>We advocate for robust and inclusive democracies where governments answer to the people they serve.</p>
    <p>Our goal is to counter the pursuit of political self-interest in favour of a sustainable future for both people and the planet, ensuring<br>that no one is left behind.</p>
    <p>What counts in life is not the mere fact that we have lived. It is what difference we have made to the lives of others that will determine the significance of the life we lead. Amara Osei</p>
  </div>
  <span class="btn" style="top:1090px;left:632px;width:125px">Learn More</span>

  <h2 class="abs values-title serif">Our Values</h2>
  <div class="abs values-list">
    <div class="value"><h3>Kindness</h3><p>The bridge that connects us all. It is the light that dissipates darkness, turning isunderstanding into harmony.</p></div>
    <div class="value"><h3>Integrity</h3><p>Our compass. Doing what is right, even when it is not popular and especially when no one is watching.</p></div>
    <div class="value"><h3>Empathy</h3><p>Seeing through others' eyes, embracing our differences, and finding common ground.</p></div>
    <div class="value"><h3>Love<span>Lumen Bright Smile</span></h3><p>The foundation of family and the force that transforms the ordinary into the extraordinary.</p></div>
    <div class="value"><h3>Education</h3><p>Amara Osei said it best: "The most powerful weapon which you can use to change the world.</p></div>
    <div class="value"><h3>Curiosity:</h3><p>The insatiable urge to explore and understand fuels human progress, paving the way for a just world and scientific breakthroughs.</p></div>
  </div>
  <div class="abs values-photo" role="img" aria-label="Statue of a sea god holding a trident amid bright splashing waves"></div>

  <h2 class="abs center section-title serif" style="top:2033px">Specifics Of Our Support</h2>
  <p class="abs center sub" style="top:2103px">Under the Lanterns supports charities and not for profits that promote:</p>
  <div class="support">
    <div class="support-item">
      <svg width="38" height="34" viewBox="0 0 38 34" fill="none" stroke="var(--heading)" stroke-width="1.3"><path d="M19 3v22M10 7h18M10 7l-5 10h10zM28 7l-5 10h10zM13 29h12M19 25v4"/></svg>
      Democracy - projects and organizations working to strengthen the foundations of democracy.</div>
    <div class="support-item">
      <svg width="38" height="34" viewBox="0 0 38 34" fill="none" stroke="var(--heading)" stroke-width="1.3"><circle cx="20" cy="10" r="4"/><path d="M20 2v2M13 6l2 1M27 6l-2 1M5 24h8l6 3h10l5-5M13 24l3-3h8"/></svg>
      Equality - projects and organizations combating the unequal distribution of opportunities across the social, economic, political, and cultural spheres.</div>
    <div class="support-item">
      <svg width="38" height="34" viewBox="0 0 38 34" fill="none" stroke="var(--heading)" stroke-width="1.3"><path d="M5 10h28v20H5zM19 10v20M9 15h7M9 19h7M22 15h7M22 19h7"/><circle cx="19" cy="5" r="3"/></svg>
      Education - initiatives that broaden the availability of education</div>
  </div>
  <span class="btn" style="top:2298px;left:537px;width:125px">Learn More</span>

  <h2 class="abs center section-title serif" style="top:2496px;color:var(--white)">Latest Posts In Our Blog</h2>
  <p class="abs center sub" style="top:2566px;color:var(--white)">Under the Lanterns supports charities and not for profits that promote:</p>
  <article class="card" style="left:122px"><div class="img" role="img" aria-label="Marble statue of a seated thinker against a golden sunset" style="background:linear-gradient(120deg,#f6c36e,#e49a52 55%,#f3dcb0)"></div><p class="date">25/04/2024</p><h4>The Second Blog</h4><p>This is where celeste, mama and Papa an write stuff</p></article>
  <article class="card" style="left:447px"><div class="img" role="img" aria-label="Weathered stone statue bust in soft teal light" style="background:linear-gradient(120deg,#5fa9b3,#a9c4c2 50%,#4a8f9c)"></div><p class="date">25/04/2024</p><h4>Blog Post With Formatting<br>Tips For You</h4></article>
  <article class="card" style="left:772px"><div class="img" role="img" aria-label="Sunken statue among bright underwater rocks" style="background:linear-gradient(120deg,#7ccfb4,#4ea88d 55%,#2f7f6c)"></div><p class="date">25/04/2024</p><h4>The Second Blog</h4><p>This is where celeste, mama and Papa an write stuff</p></article>
  <span class="btn light" style="top:2943px;left:537px;width:125px">View All</span>

  <h2 class="abs center section-title serif" style="top:3125px">Do You Need To Contact Us?</h2>
  <p class="abs center sub" style="top:3196px">Under the Lanterns supports charities and not for profits that promote:</p>
  <span class="btn" style="top:3254px;left:537px;width:125px">Get In Touch</span>

  <footer>
    <div class="abs footer-nav"><span class="brand">SHORE FOLK</span><ul><li>HOME</li><li>MISSION</li><li>WHO</li><li>FOCUS</li><li>BLOG</li><li>CONTACT</li></ul></div>
    <div class="abs footer-rule"></div>
    <p class="abs center copyright">© Copyright All Right Reserved 2024</p>
  </footer>
</div>
</body>
</html>
```